KVO-Business Card Design

I need a modern, professional business card design that includes my logo as the main feature, maybe the entire background with the contact info overlaying or even contact info on the back and the logo full frontal

Neat and organized placement of contact information

Would like to see options in black and white

Target Market(s)

real estate Developers, Construction managers, business and home owners

Industry/Entity Type

Construction

Contact Information for Business Card

KVO Construction
Danny Ferrante
General Contractor

Office: 1-888-902-7315 Ext #1
Cell: 215-730-4162
Fax: 1-888-902-7315

Font styles to use
Serif

Requirements
Must have
• title
• office #
• cell #
• Email
• website
Nice to have
• fax

```html
<!DOCTYPE html>
<html lang="en">
<head>
<meta charset="utf-8">
<title>KVO Construction – Business Card</title>
<link href="https://fonts.googleapis.com/css2?family=PT+Serif:wght@400;700&display=swap" rel="stylesheet">
<style>
  :root {
    --stage: #2b2b2b;
    --card: #ffffff;
    --green: #3f9a2a;
    --green-dark: #1f6e1c;
    --green-light: #7cc04a;
    --ink: #1a1a1a;
    --rule: #2d5f8a;
  }
  * { box-sizing: border-box; margin: 0; padding: 0; }
  html, body {
    width: 1200px; height: 849px; overflow: hidden;
    background: var(--stage);
    font-family: "PT Serif", Georgia, serif;
  }
  .canvas { position: relative; width: 1200px; height: 849px; }

  .card {
    position: absolute; width: 580px; height: 330px;
    box-shadow: 0 10px 30px rgba(0,0,0,.45);
  }

  /* Front: contact side */
  .card--front {
    left: 50px; top: 80px;
    background: linear-gradient(135deg, var(--green-dark), var(--green) 55%, var(--green-light));
    padding: 22px;
  }
  .front-panel {
    width: 100%; height: 100%;
    background: var(--card);
    border-radius: 34px;
    display: flex; align-items: center;
    padding: 0 22px;
  }
  .identity {
    width: 190px; flex: none; text-align: center;
    display: flex; flex-direction: column; align-items: center;
  }
  .brand-name {
    font-weight: 700; font-size: 48px; color: var(--green);
    letter-spacing: 2px; line-height: 1;
  }
  .brand-sub {
    font-weight: 700; font-size: 11px; color: var(--green);
    letter-spacing: 3px; margin-top: 6px; text-transform: uppercase;
  }
  .person-name {
    margin-top: 24px; font-size: 16px; color: var(--ink);
    text-transform: uppercase; letter-spacing: .5px; white-space: nowrap;
  }
  .person-title {
    font-size: 12px; color: var(--ink); text-transform: uppercase;
    margin-top: 3px; white-space: nowrap;
  }
  .divider {
    width: 2px; height: 170px; background: var(--rule); margin: 0 16px 0 14px; flex: none;
  }
  .contact { min-width: 0; }
  .contact-company {
    font-size: 18px; color: var(--ink); text-transform: uppercase;
    letter-spacing: .5px; margin-bottom: 6px; white-space: nowrap;
  }
  .contact-list { list-style: none; }
  .contact-list li {
    display: flex; align-items: center; gap: 7px;
    font-size: 13px; color: var(--ink); margin-top: 6px; white-space: nowrap;
  }
  .contact-list svg { width: 16px; height: 16px; flex: none; }

  /* Back: logo side */
  .card--back {
    left: 580px; top: 440px;
    background: var(--card);
    display: flex; flex-direction: column; align-items: center; justify-content: center;
    border-bottom: 2px solid var(--rule);
  }
  .back-mark { display: flex; align-items: center; gap: 14px; }
  .back-square { width: 26px; height: 26px; background: var(--green); }
  .back-name {
    font-weight: 700; font-size: 86px; color: var(--green);
    letter-spacing: 4px; line-height: 1;
  }
  .back-sub {
    font-weight: 700; font-size: 15px; color: var(--green);
    letter-spacing: 5px; margin-top: 12px; text-transform: uppercase;
  }
</style>
</head>
<body>
<main class="canvas">

  <section class="card card--front" aria-label="Business card front">
    <div class="front-panel">
      <div class="identity">
        <div class="brand-name">KVO</div>
        <div class="brand-sub">Construction</div>
        <div class="person-name">Danny Ferrante</div>
        <div class="person-title">(General Contractor)</div>
      </div>
      <div class="divider"></div>
      <div class="contact">
        <div class="contact-company">KVO Construction</div>
        <ul class="contact-list">
          <li>
            <svg viewBox="0 0 20 20" aria-hidden="true"><circle cx="10" cy="10" r="9" fill="none" stroke="#1a1a1a" stroke-width="1.5"/><path d="M6.5 5.5l2 .2.7 2.3-1.2 1a6 6 0 0 0 3 3l1-1.2 2.3.7.2 2c-4.5.6-8.6-3.5-8-8z" fill="#1a1a1a"/></svg>
            Office: 1-888-902-7315 Ext #1
          </li>
          <li>
            <svg viewBox="0 0 20 20" aria-hidden="true"><circle cx="10" cy="10" r="9" fill="none" stroke="#1a1a1a" stroke-width="1.5"/><rect x="7" y="4.5" width="6" height="11" rx="1" fill="none" stroke="#1a1a1a" stroke-width="1.4"/><circle cx="10" cy="13.3" r=".8" fill="#1a1a1a"/></svg>
            Cell: 215-730-4162
          </li>
          <li>
            <svg viewBox="0 0 20 20" aria-hidden="true"><circle cx="10" cy="10" r="9" fill="none" stroke="#1a1a1a" stroke-width="1.5"/><rect x="5.5" y="8" width="9" height="6" fill="none" stroke="#1a1a1a" stroke-width="1.3"/><rect x="7.5" y="5" width="5" height="3" fill="none" stroke="#1a1a1a" stroke-width="1.2"/></svg>
            Fax: 1-888-902-7315
          </li>
          <li>
            <svg viewBox="0 0 20 20" aria-hidden="true"><circle cx="10" cy="10" r="9" fill="none" stroke="#1a1a1a" stroke-width="1.5"/><rect x="5" y="6.5" width="10" height="7" fill="none" stroke="#1a1a1a" stroke-width="1.3"/><path d="M5 6.5l5 4 5-4" fill="none" stroke="#1a1a1a" stroke-width="1.3"/></svg>
            Email: danny@kvobuilds.com
          </li>
          <li>
            <svg viewBox="0 0 20 20" aria-hidden="true"><circle cx="10" cy="10" r="9" fill="none" stroke="#1a1a1a" stroke-width="1.5"/><circle cx="10" cy="10" r="5" fill="none" stroke="#1a1a1a" stroke-width="1.2"/><path d="M5 10h10M10 5c-2.2 2.8-2.2 7.2 0 10M10 5c2.2 2.8 2.2 7.2 0 10" fill="none" stroke="#1a1a1a" stroke-width="1"/></svg>
            Web: www.kvobuilds.com
          </li>
        </ul>
      </div>
    </div>
  </section>

  <section class="card card--back" aria-label="Business card back">
    <div class="back-mark">
      <div class="back-square"></div>
      <div class="back-name">KVO</div>
    </div>
    <div class="back-sub">Construction</div>
  </section>

</main>
</body>
</html>
```